Complete redesign of Licensed Medical Cannabis Dispensary website

Redesign website to modernize it and simplify it and add a self service reservation/preorder interactive delivery form. Also integrate current POS system that has current inventory. Here is a website for inspiration that I really like because of it simplicity https://www.lumo.example and easy ordering option. Attached is our logo.... please design around that and this is our website address www.brindlegatecourier.example

Font styles to use
Sans Serif

Colors
5c5c5c
cbcbcb
000000
add136

Requirements
Must have
• inventory thats integrated with pos
• online reservation/delivery form
Nice to have
• a website thats modern and simple
• The website designed are the logo that is attached
Should not have
• too much information

```html
<!DOCTYPE html>
<html lang="en">
<head>
<meta charset="utf-8">
<title>Brindlegate Greens — California Grown</title>
<link rel="stylesheet" href="https://fonts.googleapis.com/css2?family=Montserrat:wght@400;500;600;700;800&family=Open+Sans:wght@400;600;700&display=swap">
<style>
:root{
  --green:#1f861f;
  --green-dark:#16701a;
  --green-soft:#5da447;
  --leaf-pale:#cfe3bd;
  --ink:#1a1a1a;
  --grey:#5c5c5c;
  --grey-light:#cbcbcb;
  --footer:#474a47;
  --white:#ffffff;
}
*{margin:0;padding:0;box-sizing:border-box}
html,body{width:1200px;height:3035px;overflow:hidden}
body{position:relative;background:var(--white);font-family:"Montserrat",sans-serif;color:var(--ink)}
.abs{position:absolute}

/* hero */
.hero{left:0;top:0;width:1200px;height:800px;background:linear-gradient(110deg,#e9e2d8 0%,#ddd3c6 40%,#6f8a4c 62%,#2f5e22 80%,#3f6b2c 100%);overflow:hidden}
.hero-buds{left:250px;top:560px;width:480px;height:210px;border-radius:50%;background:radial-gradient(ellipse at center,#7a6a3a 0%,#8d8250 45%,rgba(150,140,100,0) 72%)}
.site-header{left:0;top:0;width:1200px;height:142px;background:rgba(60,60,60,.78)}
.brand{left:105px;top:30px;display:flex;align-items:center;gap:14px;color:var(--white)}
.brand-mark{width:78px;height:78px;border-radius:50%;background:var(--green)}
.brand-name{font-size:31px;font-weight:600;line-height:1}
.brand-tag{font-size:13px;font-weight:500;letter-spacing:3px;margin-top:6px}
.orders{left:845px;top:36px;color:var(--white);font-family:"Open Sans",sans-serif;font-weight:700;font-size:21px;display:flex;align-items:center;gap:10px}
.nav{left:518px;top:100px;color:var(--white);font-size:13px;font-weight:500}
.nav span{position:absolute;white-space:nowrap}
.hero-title{left:97px;top:398px;font-size:40px;font-weight:700;color:#111;letter-spacing:.3px;white-space:nowrap}
.btn{display:flex;align-items:center;justify-content:center;background:var(--green);color:var(--white);font-weight:700;font-size:13px}
.shop-now{left:97px;top:472px;width:152px;height:44px;text-transform:uppercase}
.dots{left:562px;top:690px;display:flex;gap:6px}
.dots i{width:14px;height:14px;border-radius:50%;background:var(--white);display:block}
.dots i.on{background:var(--green)}
.hero-wave{left:0;top:690px}

/* decorations */
.leaf-deco{border-radius:50% 50% 50% 0;background:var(--leaf-pale);opacity:.7}

/* steps */
.step{width:240px;text-align:center}
.step-ring{width:116px;height:116px;border:3px solid var(--green);border-radius:50%;margin:0 auto;display:flex;align-items:center;justify-content:center;background:var(--white)}
.step-label{margin-top:22px;font-size:18px;font-weight:700;color:var(--green)}
.step-link{top:944px;width:120px;border-top:3px dotted #9bbf8f}

/* products */
.products{left:0;top:1175px;width:1200px;height:610px;background:var(--green)}
.section-title{font-size:28px;font-weight:700;text-align:center;width:1200px;left:0}
.tabs{top:1288px;left:0;width:1200px;display:flex;justify-content:center;align-items:center;gap:26px;color:var(--white);font-size:17px;font-weight:700}
.tab-active{border:2px solid var(--white);border-radius:20px;padding:7px 26px}
.card{width:225px;text-align:center;color:var(--white)}
.card-photo{width:225px;height:182px;box-shadow:0 4px 10px rgba(0,0,0,.3)}
.card-name{margin-top:22px;height:56px;font-size:15px;font-weight:700;line-height:28px}
.card-price{font-size:15px;font-weight:700;margin-top:14px}
.card-tools{left:22px;top:72px;display:flex;gap:40px}
.card-tools b{width:34px;height:34px;background:var(--white);display:flex;align-items:center;justify-content:center}

/* about */
.about-title{left:108px;top:1932px;font-size:30px;font-weight:700;color:var(--green)}
.about-copy{left:108px;top:1990px;width:470px;font-size:15px;font-weight:700;line-height:28px;text-align:justify;color:#222}
.read-more{left:108px;top:2153px;width:170px;height:46px;border-radius:23px;font-size:16px}
.about-leaf{left:690px;top:1845px;width:390px;height:435px;background:radial-gradient(ellipse at 50% 45%,#3f8a3a 0%,#2b6a32 45%,#6e8f70 66%,rgba(255,255,255,0) 70%)}

/* testimonials */
.testimonials{left:0;top:2345px;width:1200px;height:455px;background:var(--green-soft)}
.quote-card{left:136px;top:2418px;width:928px;height:314px;background:var(--white);box-shadow:0 4px 14px rgba(0,0,0,.2)}
.quote-title{left:0;top:38px;width:928px;text-align:center;font-size:27px;font-weight:700;color:var(--green)}
.quote-back{left:48px;top:72px;width:88px;height:88px;border-radius:50%;background:var(--green)}
.quote-photo{left:84px;top:88px;width:140px;height:140px;border-radius:50%;background:linear-gradient(160deg,#d8e7f0,#9fb3c2 60%,#2d3c55);border:5px solid var(--white)}
.quote-text{left:244px;top:96px;width:640px;font-family:"Open Sans",sans-serif;font-size:15px;line-height:28px;color:#222}
.quote-by{left:552px;top:246px;font-family:"Open Sans",sans-serif;font-style:italic;font-weight:700;font-size:15px}
.quote-next{left:860px;top:28px}

/* footer */
.site-footer{left:0;top:2800px;width:1200px;height:235px;background:var(--footer);color:var(--white)}
.foot-col h3{font-size:22px;font-weight:500;margin-bottom:12px;letter-spacing:.5px}
.foot-col li{list-style:none;font-family:"Open Sans",sans-serif;font-size:15px;line-height:28px}
.foot-brand{left:750px;top:26px}
.social{left:866px;top:140px;display:flex;gap:6px}
.social i{width:24px;height:24px;border-radius:50%;background:var(--white);display:block}
.copyright{left:733px;top:207px;font-family:"Open Sans",sans-serif;font-size:14px}
</style>
</head>
<body>

<section class="hero abs" role="img" aria-label="Photograph of cannabis buds and leaves on a pale stone surface"></section>
<div class="hero-buds abs" aria-hidden="true"></div>

<header class="site-header abs">
  <div class="brand abs">
    <div class="brand-mark"></div>
    <div>
      <div class="brand-name">Brindlegate Greens</div>
      <div class="brand-tag">CALIFORNIA GROWN</div>
    </div>
  </div>
  <div class="orders abs">
    <svg width="20" height="18" viewBox="0 0 20 18"><path d="M3 6c0-3 3-4 7-4s7 1 7 4h-4V4H7v2zM4 8h12l2 8H2z" fill="#fff"/></svg>
    ORDERS: 555-010-4421
  </div>
  <nav class="nav abs">
    <span style="left:0">HOME</span>
    <span style="left:85px">ABOUT</span>
    <span style="left:179px">ALL PRODUCTS</span>
    <span style="left:325px">STORE</span>
    <span style="left:422px">CONTACT US</span>
    <span style="left:557px;top:-10px">
      <svg width="26" height="32" viewBox="0 0 26 32"><path d="M8 9V6a5 5 0 0 1 10 0v3" fill="none" stroke="#fff" stroke-width="2"/><rect x="2" y="9" width="22" height="21" fill="none" stroke="#fff" stroke-width="2"/><text x="13" y="25" fill="#fff" font-size="11" font-family="Montserrat" text-anchor="middle">0</text></svg>
    </span>
  </nav>
</header>

<h1 class="hero-title abs">BRINDLEGATE GREENS</h1>
<a class="btn shop-now abs">Shop Now</a>
<div class="dots abs"><i></i><i></i><i></i><i class="on"></i></div>
<svg class="hero-wave abs" width="1200" height="112" viewBox="0 0 1200 112"><path d="M0 112V70C120 105 260 110 420 72C560 38 700 0 860 10C1000 20 1100 40 1200 46V112Z" fill="#fff"/></svg>

<!-- steps -->
<div class="leaf-deco abs" style="left:1045px;top:780px;width:150px;height:110px" role="img" aria-label="Faint leaf decoration"></div>
<div class="leaf-deco abs" style="left:0;top:1000px;width:95px;height:160px" role="img" aria-label="Faint leaf decoration"></div>

<div class="step abs" style="left:96px;top:888px">
  <div class="step-ring"><svg width="60" height="60" viewBox="0 0 60 60" fill="none" stroke="#1f861f" stroke-width="3.5"><path d="M44 32v18H10V16h18"/><path d="M26 36l2-8 18-18 6 6-18 18z"/></svg></div>
  <div class="step-label">SIGN IN</div>
</div>
<div class="step abs" style="left:355px;top:888px">
  <div class="step-ring"><svg width="62" height="60" viewBox="0 0 62 60" fill="none" stroke="#1f861f" stroke-width="3.5"><path d="M4 10h9l7 28h30l6-20H16"/><path d="M24 24h28M26 31h24M30 18v20M38 18v20M46 18v20"/><circle cx="24" cy="46" r="4"/><circle cx="46" cy="46" r="4"/></svg></div>
  <div class="step-label">PLACE ORDER</div>
</div>
<div class="step abs" style="left:608px;top:888px">
  <div class="step-ring"><svg width="60" height="62" viewBox="0 0 60 62" fill="none" stroke="#1f861f" stroke-width="3.5"><rect x="12" y="10" width="32" height="44"/><rect x="21" y="5" width="14" height="9"/><path d="M18 24h4M26 24h12M18 32h4M26 32h12M18 40h4M26 40h6"/><circle cx="44" cy="46" r="9" fill="#1f861f"/><path d="M40 46l3 3 5-6" stroke="#fff"/></svg></div>
  <div class="step-label">GET CONFIRMATION</div>
</div>
<div class="step abs" style="left:865px;top:888px">
  <div class="step-ring"><svg width="66" height="56" viewBox="0 0 66 56" fill="none" stroke="#1f861f" stroke-width="3.5"><path d="M14 10h30v28H14zM44 18h10l8 10v10H44"/><path d="M2 18h10M4 26h8"/><circle cx="22" cy="42" r="5" fill="#fff"/><circle cx="52" cy="42" r="5" fill="#fff"/></svg></div>
  <div class="step-label">RECEIVE DELIVERY</div>
</div>
<div class="step-link abs" style="left:275px"></div>
<div class="step-link abs" style="left:535px"></div>
<div class="step-link abs" style="left:790px"></div>
<svg class="abs" style="left:330px;top:930px" width="20" height="30"><path d="M4 3l12 12-12 12" fill="none" stroke="#1f861f" stroke-width="4"/></svg>
<svg class="abs" style="left:592px;top:930px" width="20" height="30"><path d="M4 3l12 12-12 12" fill="none" stroke="#1f861f" stroke-width="4"/></svg>
<svg class="abs" style="left:847px;top:930px" width="20" height="30"><path d="M4 3l12 12-12 12" fill="none" stroke="#1f861f" stroke-width="4"/></svg>

<!-- products -->
<section class="products abs"></section>
<svg class="abs" style="left:0;top:1710px" width="1200" height="80" viewBox="0 0 1200 80"><path d="M0 0H1200V66C1060 84 900 80 740 62C560 42 380 30 220 36C120 40 50 48 0 60Z" fill="#1f861f"/><path d="M0 60C50 48 120 40 220 36C380 30 560 42 740 62C900 80 1060 84 1200 66V80H0Z" fill="#fff"/></svg>
<h2 class="section-title abs" style="top:1210px;color:#fff">PRODUCTS</h2>
<div class="tabs abs"><span>ALL</span><span class="tab-active">LEAVES</span><span>CONCENTRATE</span></div>

<div class="card abs" style="left:103px;top:1363px">
  <div class="card-photo" role="img" aria-label="Close-up photograph of green cannabis flowers" style="background:linear-gradient(135deg,#4d8a3e,#2f6a2a 55%,#5a9a48)"></div>
  <div class="card-tools abs">
    <b><svg width="18" height="18" viewBox="0 0 18 18" fill="none" stroke="#1f861f" stroke-width="2.5"><circle cx="7" cy="7" r="5"/><path d="M11 11l6 6"/></svg></b>
    <b><svg width="18" height="16" viewBox="0 0 18 16"><path d="M9 15L2 8a4 4 0 0 1 7-5 4 4 0 0 1 7 5z" fill="#1f861f"/></svg></b>
    <b><svg width="20" height="18" viewBox="0 0 20 18" fill="none" stroke="#1f861f" stroke-width="2.2"><path d="M1 2h3l3 10h10l2-7H5"/><circle cx="8" cy="15" r="1.6"/><circle cx="16" cy="15" r="1.6"/></svg></b>
  </div>
  <div class="card-name">FLOWERS</div>
  <div class="card-price">$15.00 – $30.00</div>
</div>
<div class="card abs" style="left:356px;top:1363px">
  <div class="card-photo" role="img" aria-label="Photograph of a trimmed cannabis bud" style="background:linear-gradient(135deg,#8fa865,#b8bf86 50%,#6d8c45)"></div>
  <div class="card-name">Trail Biscuit (Private Reserve)</div>
  <div class="card-price">$30</div>
</div>
<div class="card abs" style="left:615px;top:1363px">
  <div class="card-photo" role="img" aria-label="Photograph of cannabis buds" style="background:linear-gradient(135deg,#8d9a55,#b3a870 50%,#5f7a3a)"></div>
  <div class="card-name">Sticky Bond</div>
  <div class="card-price">$17.00</div>
</div>
<div class="card abs" style="left:876px;top:1363px">
  <div class="card-photo" role="img" aria-label="Photograph of dark cannabis buds" style="background:linear-gradient(135deg,#6b5a40,#a08b6a 50%,#4d4232)"></div>
  <div class="card-name">Crownstrap OZ</div>
  <div class="card-price">$5.59</div>
</div>

<!-- about -->
<div class="leaf-deco abs" style="left:1040px;top:1775px;width:150px;height:120px" role="img" aria-label="Faint leaf decoration"></div>
<div class="leaf-deco abs" style="left:0;top:2165px;width:150px;height:170px" role="img" aria-label="Faint leaf decoration"></div>
<h2 class="about-title abs">About us</h2>
<p class="about-copy abs">Lorem Ipsum is simply dummy text of the printing and typesetting industry. Lorem Ipsum has been the industry's standard dummy text ever since the 1500s, when an unknown printer took a galley of type and scrambled it to make a type specimen book.</p>
<a class="btn read-more abs">Read More</a>
<div class="about-leaf abs" role="img" aria-label="Cannabis leaf shape filled with a photograph of green buds"></div>

<!-- testimonials -->
<section class="testimonials abs" role="img" aria-label="Soft green patterned background"></section>
<div class="quote-card abs">
  <h2 class="quote-title abs">TESTIMONIALS</h2>
  <svg class="quote-next abs" width="20" height="30"><path d="M4 3l12 12-12 12" fill="none" stroke="#555" stroke-width="3"/></svg>
  <div class="quote-back abs"></div>
  <div class="quote-photo abs" role="img" aria-label="Portrait photograph of a smiling customer"></div>
  <p class="quote-text abs">“ Lorem Ipsum is simply dummy text of the printing and typesetting industry. Lorem Ipsum has been the industry's standard dummy text ever since the 1500s, when an unknown printer took a galley of type and scrambled it to make a type specimen book. It has survived not only five centuries, but also the leap into electronic typesetting, remaining essentially unchanged.”</p>
  <div class="quote-by abs">-Jack</div>
</div>

<!-- footer -->
<footer class="site-footer abs">
  <div class="foot-col abs" style="left:136px;top:22px">
    <h3>EXPLORE</h3>
    <ul><li>Store</li><li>Cart</li><li>My Account</li><li>New Patient Verification</li><li>Contact Us</li></ul>
  </div>
  <div class="foot-col abs" style="left:434px;top:22px">
    <h3>FORUMS</h3>
    <ul><li>Bongs, Bubblers, &amp; Water Pipes</li><li>Concentrates</li><li>Growing</li><li>Vaporizers</li><li>What Are You Smokin'?</li></ul>
  </div>
  <div class="brand foot-brand abs">
    <div class="brand-mark" style="width:64px;height:64px"></div>
    <div>
      <div class="brand-name" style="font-size:26px">Brindlegate Greens</div>
      <div class="brand-tag">CALIFORNIA GROWN</div>
    </div>
  </div>
  <div class="social abs"><i></i><i></i><i></i><i></i></div>
  <div class="copyright abs">Copyrights © 2018 . ALL RIGHTS RESERVED.</div>
</footer>

</body>
</html>
```